Project Overview:
We are looking to create a website for a monthly subscription IPTV service in WordPress. The website should provide a seamless user experience for customers to sign up for the service and manage their account information. We need the following pages: Home Page, Product Page, Sign-Up Page, and Account Information Page.

Home Page:
The Home Page design should be simple and clean, with a dark theme and minimalistic design elements. We would like to include graphics of popular movie shows displayed on multiple devices. The page should highlight the key benefits and features of our service and provide a clear call-to-action for visitors to sign up.

Product Page:
The Product Page should provide detailed information about our subscription tiers and pricing plans. It should highlight the key features of each plan and provide a clear comparison between them. The page should also include a call-to-action button for visitors to sign up.

Sign-Up Page:
The Sign-Up Page is the conversion page where members will sign up for the service. It should collect the following information: Name, Phone Number, Email, Password, and Payment Information. The design should be simple, intuitive, and easy to use. It should highlight the benefits of our service and provide a clear call-to-action for visitors to sign up.

Account Information Page:
The Account Information Page should allow members to view and manage their account details. It should include the following information: Profile Image, Contact Details, Password Management, Payment Information Management, and Membership Expiration Date. The design should be user-friendly, intuitive, and easy to navigate.

Goals: The primary goal of the website is to provide an easy-to-use portal for customers to sign up for the service and manage their account information. The website should be user-friendly and visually appealing to attract potential customers.

Scope: The scope of the project includes designing a home page, a sign-up page, an account information page, and a payment information page. The website should be designed to be responsive and accessible on desktop and mobile devices.

Design Preferences: The design should be clean, modern, and visually appealing. The use of a color palette that is consistent with the brand identity is recommended. The website should be easy to navigate and provide a clear call-to-action for users to sign up for the service.

FYI: The subscription service I am designing a website for is related to an IPTV service. IPTV stands for Internet Protocol Television, which is a digital television broadcasting protocol that uses the internet to deliver TV programs and videos to viewers. The website will allow customers to sign up for the IPTV service and access their account information such as user name and password, membership tier, name, and payment details. Please let me know if you have any further questions, and I would be happy to provide more details. Thank you!

Dear Designers,

Thank you for your participation in our project. After reviewing the designs received so far, we have decided to update the brief to better reflect our needs and preferences. We apologize for any confusion this may cause, but we believe that these changes will result in better design submissions and a more successful project overall.

The updated brief is as follows:

We are looking to create a website for WordPress.

Also, here is the updated Brief.

Project Title: WordPress Website Design for Monthly Subscription IPTV Service

Project Overview:
We are looking to create a website for a monthly subscription IPTV service. The website should provide a seamless user experience for customers to sign up for the service and manage their account information. We need the following pages: Home Page, Product Page, Sign-Up Page, and Account Information Page.

Home Page:

Product Page:

Sign-Up Page:

Account Information Page:

Design Preferences:
We prefer a dark theme with minimalistic design elements and hits of our logo colors. The website should be easy to use and navigate, with clear calls-to-action and simple, intuitive forms. The design should be optimized for mobile devices and load quickly.

We hope that these updates provide you with a clearer understanding of our requirements and preferences. Please let us know if you have any questions or concerns. We look forward to seeing your revised designs.

Thank you again for your participation.
We will guarantee this project as soon as we see something we like that meets the updated requirements.

The website's target audience is individuals who are interested in subscribing to the monthly service.

• One item for sale and a client profile section.

```html
<!DOCTYPE html>
<html lang="en">
<head>
<meta charset="utf-8">
<title>Vistora – Stream Everything</title>
<link rel="stylesheet" href="https://fonts.googleapis.com/css2?family=Poppins:wght@400;500;600;700;800&display=swap">
<style>
  :root{
    --red:#ff0000;
    --ink:#ffffff;
    --night:#0a0f1f;
    --navy:#0a1a6b;
    --coal:#141416;
    --slate:#2b2b2d;
    --field:#2c2c2e;
    --font:'Poppins', sans-serif;
  }
  *{box-sizing:border-box;margin:0;padding:0}
  html,body{width:1200px;height:3107px;overflow:hidden}
  body{position:relative;background:var(--coal);font-family:var(--font);color:var(--ink)}
  .abs{position:absolute}
  .backdrop{position:absolute;left:0;top:0}
  .media{position:absolute}

  /* header */
  .brand{left:133px;top:24px;width:160px;height:56px;display:flex;align-items:center;gap:10px;font-weight:800;font-size:26px;color:var(--ink)}
  .brand .dot{width:16px;height:16px;background:var(--red);border-radius:50%}
  .nav a{position:absolute;top:45px;font-size:15px;color:var(--ink);text-decoration:none;font-weight:400}
  .btn{position:absolute;display:flex;align-items:center;justify-content:center;background:var(--red);color:var(--ink);border-radius:28px;font-weight:600;text-decoration:none}
  .signup{left:1038px;top:33px;width:112px;height:43px;font-size:15px;font-weight:700}

  /* hero */
  .hero-panel{left:193px;top:215px;width:808px;height:249px;background:rgba(20,18,20,.55)}
  .hero-title{left:0;width:1232px;top:255px;text-align:center;font-weight:800;font-size:56px;line-height:62px;letter-spacing:-1px}
  .hero-sub{left:0;width:1232px;top:403px;text-align:center;font-weight:600;font-size:21px}
  .hero-btn{width:253px;height:58px;top:465px;font-size:20px}

  /* section headings */
  .kicker{color:var(--red);font-weight:600;font-size:40px;line-height:48px}
  .copy{font-size:16.5px;line-height:29px;text-align:center}

  /* form */
  .label{font-size:16px;font-weight:400}
  .field{background:var(--field);border-radius:14px;height:58px}
  .pay{left:123px;top:2281px;width:353px;height:58px;font-size:20px}

  .plans{right:118px;text-align:right;font-weight:600}
  .plans .plan{font-size:27px;line-height:33px}
  .plans .note{font-size:22px;line-height:28px}

  /* cta */
  .cta-line{left:643px;top:2496px;font-size:26px;font-weight:400}

  /* footer */
  .foot-brand{left:121px;top:2792px;display:flex;align-items:center;gap:12px;font-weight:800;font-size:46px;line-height:54px}
  .foot-brand .dot{width:22px;height:22px;background:var(--red)}
  .foot-copy{left:125px;top:2868px;width:340px;font-size:16.5px;line-height:34px}
  .col h4{color:var(--red);font-weight:400;font-size:26px;line-height:32px;margin-bottom:6px}
  .col li{list-style:none;font-size:16px;line-height:34px}
  .social{position:absolute;top:2952px;width:23px;height:23px;background:var(--ink);border-radius:4px}
  .legal{left:0;top:3063px;width:1200px;height:44px;background:var(--red);display:flex;align-items:center;justify-content:center;font-size:14px}
</style>
</head>
<body>

<svg class="backdrop" width="1200" height="3107" viewBox="0 0 1200 3107" aria-hidden="true">
  <defs>
    <linearGradient id="navyFade" x1="0" y1="0" x2="1" y2="1">
      <stop offset="0" stop-color="#050a18"/>
      <stop offset=".55" stop-color="#07113a"/>
      <stop offset="1" stop-color="#0b1d8a"/>
    </linearGradient>
    <linearGradient id="deviceFade" x1="0" y1="0" x2="1" y2="0">
      <stop offset="0" stop-color="#070c1c"/>
      <stop offset=".6" stop-color="#0d1a3e"/>
      <stop offset="1" stop-color="#1a2238"/>
    </linearGradient>
    <linearGradient id="heroFade" x1="0" y1="0" x2="1" y2="0">
      <stop offset="0" stop-color="#7a3a34"/>
      <stop offset=".45" stop-color="#3a2a2e"/>
      <stop offset="1" stop-color="#0c0a0c"/>
    </linearGradient>
    <linearGradient id="ctaFade" x1="0" y1="0" x2="1" y2="0">
      <stop offset="0" stop-color="#2c3d48"/>
      <stop offset=".45" stop-color="#2b2b2d"/>
      <stop offset="1" stop-color="#2b2b2d"/>
    </linearGradient>
    <radialGradient id="footGlow" cx="1" cy=".3" r=".5">
      <stop offset="0" stop-color="#5a3a9a"/>
      <stop offset="1" stop-color="#141416" stop-opacity="0"/>
    </radialGradient>
  </defs>
  <rect x="0" y="600" width="1200" height="760" fill="url(#navyFade)"/>
  <polygon points="0,1330 1200,1180 1200,1860 0,1770" fill="url(#deviceFade)"/>
  <polygon points="0,1770 760,1867 543,2442 0,2475" fill="var(--coal)"/>
  <polygon points="724,1867 760,1867 589,2436 543,2442" fill="var(--slate)"/>
  <polygon points="760,1867 1200,1857 1200,2340 589,2436" fill="var(--red)"/>
  <polygon points="1200,2340 1200,2440 543,2442 589,2436" fill="var(--slate)"/>
  <polygon points="0,2475 543,2442 1200,2436 1200,2717 0,2717" fill="url(#ctaFade)"/>
  <rect x="0" y="2717" width="1200" height="346" fill="var(--coal)"/>
  <rect x="900" y="2717" width="300" height="346" fill="url(#footGlow)"/>
</svg>

<!-- hero -->
<div class="media" role="img" aria-label="Wall of glowing TV screens with a hand holding a remote control" style="left:0;top:0;width:1200px;height:670px;background:linear-gradient(90deg,#7a3a34,#3a2a2e 45%,#0c0a0c);clip-path:polygon(0 0,100% 0,100% 100%,0 93.5%)"></div>
<div class="abs hero-panel"></div>

<header>
  <div class="abs brand"><span class="dot"></span>VISTORA</div>
  <nav class="nav">
    <a style="left:502px">HOME</a>
    <a style="left:591px">MOVIES</a>
    <a style="left:709px">TV SHOWS</a>
    <a style="left:838px">VIDEO</a>
    <a style="left:941px">PAGES</a>
  </nav>
  <a class="btn signup">SIGN UP</a>
</header>

<h1 class="abs hero-title">THE GREATEST CONTENT<br>ALL IN ONE PLACE</h1>
<p class="abs hero-sub">Watch unlimited movies, tv shows, and much more</p>
<a class="btn hero-btn" style="left:311px">VIEW ALL DEMOS</a>
<a class="btn hero-btn" style="left:632px">PURCHASE NOW</a>

<!-- enjoy -->
<div class="media" role="img" aria-label="Flat TV showing an explorer in a crystal cave" style="left:109px;top:778px;width:486px;height:265px;border:3px solid #555;border-radius:8px;background:linear-gradient(180deg,#1c6f86,#123844 55%,#1a1e22)"></div>
<div class="abs" style="left:338px;top:1043px;width:28px;height:22px;background:#2a2a2a"></div>
<div class="abs" style="left:193px;top:1065px;width:318px;height:6px;background:#2a2a2a;border-radius:3px"></div>
<h2 class="abs kicker" style="left:638px;top:797px">ENJOY YOUR CONTENT</h2>
<p class="abs copy" style="left:620px;top:877px;width:460px">Lorem ipsum dolor sit amet, consectetur adipiscing elit, sed do eiusmod tempor incididunt ut labore et dolore magna aliqua.</p>
<a class="btn" style="left:721px;top:1013px;width:255px;height:58px;font-size:20px">VIEW VIDEO LIBRARY</a>

<!-- devices -->
<h2 class="abs kicker" style="left:142px;top:1469px">WATCH ON ANY DEVICE</h2>
<p class="abs copy" style="left:139px;top:1557px;width:440px">Lorem ipsum dolor sit amet, consectetur adipiscing elit, sed do eiusmod tempor incididunt ut labore et dolore magna aliqua.</p>
<div class="media" role="img" aria-label="Laptop showing superhero movie scene" style="left:609px;top:1562px;width:479px;height:319px;border:8px solid #bfc3c8;border-radius:8px;background:linear-gradient(135deg,#a33a1e,#3b2a2c 55%,#b84a22)"></div>
<div class="media" role="img" aria-label="Phone showing a sci-fi movie" style="left:534px;top:1694px;width:97px;height:151px;border:4px solid #ccc;border-radius:12px;background:linear-gradient(180deg,#c9b48c,#5d5a52)"></div>
<div class="media" role="img" aria-label="Tablet showing a space series" style="left:1005px;top:1685px;width:195px;height:233px;border:6px solid #111;border-radius:10px;background:radial-gradient(circle at 50% 50%,#4a6a9c,#15203a 70%)"></div>

<!-- sign-up form -->
<form>
  <label class="abs label" style="left:147px;top:1912px">Name *</label>
  <div class="abs field" style="left:124px;top:1955px;width:350px"></div>
  <label class="abs label" style="left:145px;top:2036px">Password *</label>
  <div class="abs field" style="left:124px;top:2073px;width:350px"></div>
  <label class="abs label" style="left:147px;top:2154px">Membership tier *</label>
  <div class="abs field" style="left:121px;top:2190px;width:349px"></div>
  <a class="btn pay">PAYMENT DETAILS</a>
</form>

<div class="abs plans" style="top:1995px">
  <div class="plan">FREE - FREE / 15 DAYS</div>
  <div class="note">Valid for 15 days</div>
  <div class="plan" style="margin-top:32px">PREMIUM - 199$ / 1 MONTH</div>
  <div class="plan" style="margin-top:30px">STANDARD - 99$ / 1 MONTH</div>
  <div class="plan" style="margin-top:30px">BASIC - 29$ / 1 MONTH</div>
</div>

<!-- cta -->
<div class="media" role="img" aria-label="Faded wall of screens in front of a world map" style="left:0;top:2480px;width:540px;height:237px;background:linear-gradient(90deg,rgba(60,90,110,.6),rgba(43,43,45,0))"></div>
<p class="abs cta-line">Get Unlimited Movies &amp; TV Access</p>
<a class="btn" style="left:826px;top:2574px;width:255px;height:58px;font-size:20px">CHOOSE A PLAN</a>

<!-- footer -->
<footer>
  <div class="abs foot-brand"><span class="dot"></span>VISTORA</div>
  <p class="abs foot-copy">Lorem ipsum dolor sit amet, consectetur adipiscing elit, sed do eiusmod tempor incididunt ut labore et dolore magna aliqua.</p>
  <div class="abs col" style="left:556px;top:2802px"><h4>Explore</h4><ul><li>Movies</li><li>Series</li><li>Watchlist</li><li>Podcasts</li></ul></div>
  <div class="abs col" style="left:720px;top:2802px"><h4>Account</h4><ul><li>Choose a plan</li><li>Landing Page</li><li>My Account</li><li>Contact</li></ul></div>
  <div class="abs col" style="left:907px;top:2802px"><h4>Contact</h4><ul><li>66 Lorem ipsum dolor</li><li>+1 88888 88888</li><li>@vistora.tv</li></ul></div>
  <span class="social" style="left:907px"></span>
  <span class="social" style="left:949px"></span>
  <span class="social" style="left:992px"></span>
  <div class="abs legal">© Copyright VISTORA.tv All Rights Reserved.</div>
</footer>

</body>
</html>
```